Notary Signing Agent Need Business card Design

Need a Business card design for my new company. RT Velo-Brisk LLC
Mobile Notary Signing Agent. I go to the customer for closing of Mortgage's Documents . possible signs of honesty, integrity and confidentiality.

Work with Title company to Notary Mortgage closing.

My Target Market is Title companies. Banks and Financial Institution.

Color Blue to Black Professional ) if needed some Green Little Red

And possible a company logo.

Mobile ( travel to clients ) Integrity, Honest Trustworthy. A show of Professional services.

Would like company name and my name on card

Use both sides and front with business name and my name. phone numbers.

Target Market(s)

Title company, Banks mortgage company

Industry/Entity Type

Travel

Contact Information for Business Card

Notary, Certified signing agent, Mobile

Colors
0455a3

Requirements
Must have
• Name of company , owners name phone number,
Nice to have
• blue and black color like a professional look but not limit to these only.
• a stand out from other cards .

```html
<!DOCTYPE html>
<html lang="en">
<head>
<meta charset="utf-8">
<title>RT Velo-Brisk LLC – Business Card</title>
<link rel="stylesheet" href="https://fonts.googleapis.com/css2?family=Open+Sans:wght@300;400;600;700&display=swap">
<style>
  :root {
    --backdrop: #e6e6e6;
    --blue-deep: #2553a0;
    --blue-soft: #6f8ec1;
    --white: #ffffff;
    --ink: #111111;
    --label: #8a8a8a;
  }
  * { margin: 0; padding: 0; box-sizing: border-box; }
  html, body {
    width: 1200px; height: 960px; overflow: hidden;
    background: var(--backdrop);
    font-family: "Open Sans", Arial, sans-serif;
  }
  .sheet { position: relative; width: 1200px; height: 960px; }
  .card {
    position: absolute; width: 560px; height: 320px; overflow: hidden;
    color: var(--white);
    box-shadow: 0 6px 18px rgba(0,0,0,0.18);
  }
  .card--front { left: 300px; top: 110px; }
  .card--back  { left: 300px; top: 530px; }
  .card__art { position: absolute; inset: 0; }
  .side-label {
    position: absolute; left: 890px; font-size: 20px; font-weight: 400;
    color: var(--label); letter-spacing: 0.5px;
  }
  .side-label--front { top: 250px; }
  .side-label--back  { top: 670px; }

  .brand { position: absolute; font-weight: 600; color: var(--white); line-height: 1; }
  .brand__suffix { display: block; font-size: 54px; letter-spacing: 2px; }
  .brand__name { display: block; font-size: 15px; letter-spacing: 1px; margin-top: 2px; }

  .holder { position: absolute; }
  .holder__name { font-size: 22px; font-weight: 300; letter-spacing: 0.5px; }
  .holder__name strong { font-weight: 700; }
  .holder__role { font-size: 9px; letter-spacing: 0.6px; margin-top: 1px; text-transform: uppercase; }

  .contact { position: absolute; list-style: none; }
  .contact__item { display: flex; align-items: center; gap: 9px; font-size: 11px; margin-bottom: 6px; }
  .contact__icon { width: 15px; height: 15px; flex: none; }
</style>
</head>
<body>
<main class="sheet">

  <!-- Front side -->
  <section class="card card--front" aria-label="Business card front">
    <svg class="card__art" viewBox="0 0 560 320" aria-hidden="true">
      <rect width="560" height="320" fill="var(--blue-deep)"/>
      <polygon fill="var(--blue-soft)" points="0,0 225,0 229,14 223,30 231,48 226,66 234,84 229,104 237,124 232,146 240,168 235,190 243,214 238,236 246,260 241,284 249,304 245,320 0,320"/>
      <polygon fill="var(--white)" points="252,0 480,0 455,36 268,36"/>
      <polygon fill="var(--white)" points="0,282 130,282 158,320 0,320"/>
      <g stroke="var(--white)" stroke-width="0.8" opacity="0.85">
        <line x1="0" y1="100" x2="560" y2="100"/>
        <line x1="0" y1="108" x2="560" y2="108"/>
        <line x1="0" y1="116" x2="560" y2="116"/>
      </g>
    </svg>
    <div class="brand" style="left:228px; top:122px;">
      <span class="brand__suffix">LLC</span>
      <span class="brand__name">RT VELO-BRISK</span>
    </div>
    <div class="holder" style="left:30px; top:138px;">
      <p class="holder__name">DANIEL R <strong>HALE</strong></p>
      <p class="holder__role">Notary Signing Agent</p>
    </div>
    <ul class="contact" style="left:322px; top:248px;">
      <li class="contact__item">
        <svg class="contact__icon" viewBox="0 0 16 16"><rect width="16" height="16" rx="3" fill="var(--ink)"/><path d="M4 9.5c0-2 1.8-3.5 4-3.5s4 1.5 4 3.5v1H4z" fill="var(--white)"/><rect x="5" y="4" width="6" height="1.5" rx="0.7" fill="var(--white)"/></svg>
        <span>555-014-2231</span>
      </li>
      <li class="contact__item">
        <svg class="contact__icon" viewBox="0 0 16 16"><rect width="16" height="16" rx="3" fill="var(--ink)"/><rect x="5" y="3" width="6" height="10" rx="1" fill="none" stroke="var(--white)" stroke-width="1.2"/><circle cx="8" cy="11.3" r="0.7" fill="var(--white)"/></svg>
        <span>555-017-6640</span>
      </li>
    </ul>
  </section>
  <p class="side-label side-label--front">FRONT SIDE</p>

  <!-- Back side -->
  <section class="card card--back" aria-label="Business card back">
    <svg class="card__art" viewBox="0 0 560 320" aria-hidden="true">
      <rect width="560" height="320" fill="var(--blue-deep)"/>
      <polygon fill="var(--blue-soft)" points="0,0 280,0 285,16 279,34 287,52 282,72 290,92 284,114 292,136 287,158 295,180 289,204 297,228 291,252 299,276 294,300 300,320 0,320"/>
      <polygon fill="var(--white)" points="0,230 82,230 100,320 0,320"/>
      <polygon fill="var(--white)" points="560,200 560,320 470,320 530,228"/>
      <g stroke="var(--white)" stroke-width="0.8" opacity="0.85">
        <line x1="170" y1="72" x2="560" y2="72"/>
        <line x1="170" y1="80" x2="560" y2="80"/>
        <line x1="170" y1="88" x2="560" y2="88"/>
      </g>
    </svg>
    <div class="brand" style="left:30px; top:22px;">
      <span class="brand__suffix">LLC</span>
      <span class="brand__name">RT Velo-Brisk</span>
    </div>
    <div class="holder" style="left:105px; top:168px;">
      <p class="holder__name">DANIEL R <strong>HALE</strong></p>
      <p class="holder__role">Notary Signing Agent</p>
    </div>
    <ul class="contact" style="left:330px; top:232px;">
      <li class="contact__item">
        <svg class="contact__icon" viewBox="0 0 16 16"><rect width="16" height="16" rx="3" fill="var(--ink)"/><path d="M4 9.5c0-2 1.8-3.5 4-3.5s4 1.5 4 3.5v1H4z" fill="var(--white)"/><rect x="5" y="4" width="6" height="1.5" rx="0.7" fill="var(--white)"/></svg>
        <span>555-014-2231</span>
      </li>
      <li class="contact__item">
        <svg class="contact__icon" viewBox="0 0 16 16"><rect width="16" height="16" rx="3" fill="var(--ink)"/><rect x="5" y="3" width="6" height="10" rx="1" fill="none" stroke="var(--white)" stroke-width="1.2"/><circle cx="8" cy="11.3" r="0.7" fill="var(--white)"/></svg>
        <span>555-017-6640</span>
      </li>
    </ul>
  </section>
  <p class="side-label side-label--back">BACK SIDE</p>

</main>
</body>
</html>
```